FALKENHOF KONTOR KAFFEECATERING AUF MESSEN & EVENTS
Wir bieten ein hochwertiges Barista Catering inklusive komplettem Messe-Full- service an. Unser professionell geschultes Barista-Team sorgt für optimalen Kaffeege- nuss auf Messen, Kongressen und Events aller Art. Der elegante Abschluss mit einem Muster auf der Tasse, genannt „Latte Art“ , ist das Highlight unserer Dienstleistung.
Ob fest integriert im Messestand, als mobi- le Espressobar mit eigener Theke oder als Coffeebike- wir haben für jeden Anlass die passende Variante.
Branden Sie unser Equipment mit Ihrem Firmenlogo! Gerne beraten wir Sie hierzu.
HOSTESSENAGENTUR
Wählen Sie aus über 8.000 Hostessen und und mehr als 20 Sprachen! Unsere Hostes- sen und Hosts begleiten Sie auf:
• Messen
• Kongresse
• VIP-Veranstaltungen • Promotion
• Events aller Art
COCKTAIlS & SMOOTHIES MIT FIRMENlOGO
Unser mobiler Cocktailservice eignet sich für jede Art von Veranstaltung und ist eine geniale Ergänzung zu jedem Messestand.
Erweitern Sie das bestehende Cocktailan- gebot mit gebrandeten Smoothies in fünf verschiedenen Geschmacksrichtungen.
MESSECATERING
Egal ob klassische Häppchen, trendiges Finger- food oder Menüs in allen Variationen - sprechen Sie uns an!
Kurzum, unser Schwerpunkt liegt auf Barista-und Personalservice. An 3 Standorten-München, Berlin, Frankfurt.
Wir möchten gerne einen monatlichen Newsletter raussenden, den wir mittel MailChimp selber pflegen können. Nur brauchen wir eben dazu ein Design/Template was veränderbar ist.
Wir freuen uns auf tolle Designs!

```html
<!DOCTYPE html>
<html lang="de">
<head>
<meta charset="utf-8">
<title>Newsletter – Cocktails &amp; Messecatering</title>
<link href="https://fonts.googleapis.com/css2?family=EB+Garamond:wght@500;600&family=Montserrat:wght@400&display=swap" rel="stylesheet">
<style>
  :root {
    --page-bg: #e9e6e1;
    --paper: #ffffff;
    --night: #141414;
    --night-soft: #1e1e1e;
    --bronze: #7d5a3c;
    --bronze-heading: #7a5b3f;
    --ink: #2a2a2a;
    --ink-light: #eeeeee;
    --rule-dark: #4a4a4a;
    --rule-light: #9a9a9a;
  }
  * { box-sizing: border-box; margin: 0; padding: 0; }
  html, body {
    width: 1200px; height: 800px; overflow: hidden;
    background: var(--page-bg);
  }
  .newsletter {
    position: absolute; left: 280px; top: 0;
    width: 640px; height: 800px;
    background: var(--paper);
    overflow: hidden;
  }
  .button {
    display: inline-block;
    background: var(--bronze);
    color: #ffffff;
    font-family: "EB Garamond", serif;
    font-weight: 600;
    font-size: 20px;
    letter-spacing: 0.3px;
    padding: 12px 34px;
    text-decoration: none;
  }
  .intro-strip {
    position: relative;
    height: 110px;
    text-align: center;
    padding-top: 28px;
  }
  .photo-coffee {
    position: absolute; right: 0; top: 34px;
    width: 150px; height: 120px;
    background: linear-gradient(135deg, #f4f2ee 0%, #d9cfc0 55%, #8a6a4a 100%);
    z-index: 2;
  }
  .section-cocktails {
    position: relative;
    height: 380px;
    background: linear-gradient(160deg, var(--night) 0%, var(--night-soft) 100%);
    text-align: center;
    padding: 50px 60px 0;
  }
  .section-title {
    font-family: "EB Garamond", serif;
    font-weight: 500;
    font-size: 42px;
    line-height: 1.1;
    letter-spacing: 1px;
    color: var(--bronze-heading);
  }
  .rule {
    width: 56px; height: 3px;
    margin: 20px auto 18px;
    background: var(--rule-dark);
  }
  .section-text {
    font-family: "Montserrat", sans-serif;
    font-size: 13px;
    line-height: 1.6;
    color: var(--ink-light);
    margin-bottom: 26px;
  }
  .photo-mint {
    position: absolute; left: 0; bottom: -40px;
    width: 110px; height: 150px;
    background: radial-gradient(ellipse at 55% 45%, #8fdc3a 0%, #4fae1e 55%, #2f7a12 100%);
    border-radius: 40% 55% 45% 50%;
    z-index: 2;
  }
  .section-catering {
    position: relative;
    height: 310px;
    text-align: center;
    padding: 54px 70px 0;
  }
  .section-catering .rule { background: var(--rule-light); }
  .section-catering .section-text { color: var(--ink); }
</style>
</head>
<body>
  <main class="newsletter">
    <section class="intro-strip">
      <a class="button" href="#">Jetzt informieren</a>
      <div class="photo-coffee" role="img" aria-label="Foto einer weißen Kaffeetasse auf Jutestoff mit Kaffeebohnen"></div>
    </section>

    <section class="section-cocktails">
      <h2 class="section-title">Cocktails &amp; Smoothies<br>mit Firmenlogo</h2>
      <div class="rule"></div>
      <p class="section-text">Unser mobiler Cocktailservice eignet sich für jede Art von Veranstaltung und ist eine geniale Ergänzung zu jedem Messestand. Erweitern Sie das bestehende Cocktailangebot mit gebrandeten Smoothies in fünf verschiedenen Geschmacksrichtungen.</p>
      <a class="button" href="#">Jetzt informieren</a>
      <div class="photo-mint" role="img" aria-label="Foto frischer grüner Minzblätter"></div>
    </section>

    <section class="section-catering">
      <h2 class="section-title">Messecatering</h2>
      <div class="rule"></div>
      <p class="section-text">Egal ob klassische Häppchen, trendiges Fingerfood oder Menüs in allen Variationen – sprechen Sie uns an!</p>
      <a class="button" href="#">Jetzt informieren</a>
    </section>
  </main>
</body>
</html>
```